A website for a green bio-plastics manufacturing company

We need a home page designed and two complimentary template pages that can be used for the rest of the website. The template page should vary in design from the home page, but should flow uniformly with it.

This is a very innovative company with a proprietary manufacturing method of using bird feathers to make plastic.

The site should be functional, informative, user-friendly and informative to both our business partners and the consumers.
Updates

I've added a more concise overview of the company.  If any of the designers have any questions for me, please ask.  Thanks

Marco

Target Market(s)

Business partners interested in using bio-plastics for their products and general customers.

Industry/Entity Type

Manufacturing

Number of Pages Required

3 pages

Requirements
Must have
• I attached some information about the company, so the site should be designed to incorporate that content.

Will need to be edited by Adobe Contribute.

Easy to navigate

One of the template pages should have one column for content. The other should have two columns. I''m open to different ideas though.

Should be very pleasing to the eye and uncluttered.

Want to be informative to both our business partners as well as consumers who may be researching our product(s)

Easy to Maintain

Anticipated Tabs/Pages
· Home Page
o General “welcome” page

· About Us
o Company overview and information

· Products
o Horticulture Containers
o Agriculture Films
o Where to Buy
o Upcoming Products

· Business Partners

· Press Releases

· Contact Us

Nice to have
• Would like to have earth tones and or nice greens in the color scheme. They make use of bird feathers for their manufacturing process, so perhaps a real sharp image of a feather can be incorporated into the design. Be creative though.

Perhaps a jQuery nav bar, but that may be out of scope.

Should not have
• No flash at all.

```html
<!DOCTYPE html>
<html lang="en">
<head>
<meta charset="utf-8">
<title>Meadowline Bioplastics</title>
<link href="https://fonts.googleapis.com/css2?family=PT+Sans+Narrow:wght@400;700&family=Arimo:wght@400;700&display=swap" rel="stylesheet">
<style>
:root{
  --bg-dark:#0a5433;
  --bg-mid:#0c7646;
  --cream:#faf8ef;
  --nav:#4cb520;
  --nav-dark:#3a9415;
  --mint:#ccf0c4;
  --brand:#17804a;
  --ink:#2a2a2a;
  --body:#5a5a5a;
  --link:#3aa61a;
  --grey-btn:#6d6a66;
  --footer-text:#e6f2ea;
}
*{margin:0;padding:0;box-sizing:border-box}
html,body{width:766px;height:1200px;overflow:hidden}
body{position:relative;background:linear-gradient(90deg,var(--bg-dark),var(--bg-mid) 50%,var(--bg-dark));font-family:"Arimo",Arial,sans-serif;color:var(--body)}
.narrow{font-family:"PT Sans Narrow",Arial,sans-serif}
.page{position:absolute;left:96px;width:574px;background:#fff;box-shadow:0 0 6px rgba(0,0,0,.35)}
.header{position:absolute;left:0;top:0;width:574px;height:72px;background:linear-gradient(#fff,var(--cream))}
.brand{position:absolute;left:12px;top:20px;display:flex;align-items:center;gap:6px;font-family:"PT Sans Narrow",sans-serif;font-size:19px;font-weight:700;color:var(--ink);letter-spacing:.3px}
.brand i{display:block;width:26px;height:26px;border-radius:50%;background:var(--brand)}
.phone{position:absolute;right:12px;top:48px;font-family:"PT Sans Narrow",sans-serif;font-size:11.5px;color:#555}
.phone b{color:var(--brand)}
.nav{position:absolute;left:0;top:73px;width:574px;height:31px;background:var(--nav);border-top:1px solid var(--nav-dark)}
.nav span{position:absolute;top:9px;font-family:"PT Sans Narrow",sans-serif;font-weight:700;font-size:8.6px;color:#fff;text-transform:uppercase}
.nav .dd::after{content:"";display:inline-block;margin-left:3px;border:2px solid transparent;border-top:3px solid #8fdc6d;vertical-align:middle}
.search{position:absolute;left:409px;top:7px;width:117px;height:15px;background:#f4f4f4;border:1px solid #d6d6d6;font-size:6px;color:#666;padding:4px 0 0 16px}
.search svg{position:absolute;left:3px;top:3px}
.submit{position:absolute;left:528px;top:6px;width:34px;height:17px;background:var(--grey-btn);color:#fff;font-family:"PT Sans Narrow",sans-serif;font-weight:700;font-size:8px;text-align:center;line-height:17px}
.photo{position:absolute;background:radial-gradient(ellipse at 45% 45%,#6b4e36 0%,#3d2b1e 25%,rgba(230,240,228,.6) 55%,rgba(230,240,228,0) 75%)}
p{font-size:6.6px;line-height:10.1px}
.ticks{list-style:none}
.ticks li{position:relative;padding-left:12px;font-size:6.6px;line-height:10.1px;margin-bottom:7.5px}
.ticks svg{position:absolute;left:0;top:2px}
.footer{position:absolute;left:108px;width:550px;font-size:6.5px;color:var(--footer-text);display:flex;justify-content:space-between}
.footer nav a{color:var(--footer-text);text-decoration:none}
h2{font-family:"PT Sans Narrow",sans-serif;font-weight:400;font-size:17px;color:#111}
h2 b{color:var(--brand)}
</style>
</head>
<body>

<!-- Home page -->
<section class="page" style="top:0;height:663px">
  <div class="header">
    <div class="brand"><i></i>Meadowline Bioplastics</div>
    <div class="phone">Contact Us Today! <b>(123) 456 789</b></div>
  </div>
  <div class="nav">
    <span style="left:11px">Home</span><span class="dd" style="left:54px">About Us</span><span class="dd" style="left:108px">Products</span><span style="left:166px">Business Partners</span><span style="left:255px">Press Releases</span><span style="left:329px">Contact Us</span>
    <div class="search"><svg width="9" height="9" viewBox="0 0 9 9"><circle cx="3.6" cy="3.6" r="2.6" fill="none" stroke="#777" stroke-width="1.1"/><line x1="5.5" y1="5.5" x2="8.3" y2="8.3" stroke="#777" stroke-width="1.3"/></svg>Search</div>
    <div class="submit">SUBMIT</div>
  </div>
  <div class="hero" style="position:absolute;left:0;top:104px;width:574px;height:180px;background:linear-gradient(180deg,var(--mint),#c6eebf)">
    <div class="photo" role="img" aria-label="Sharp close-up of a brown bird feather" style="left:14px;top:6px;width:196px;height:156px"></div>
    <div class="narrow" style="position:absolute;left:245px;top:24px;font-size:27px;color:var(--brand)">A good slogan here</div>
    <p style="position:absolute;left:245px;top:62px;width:292px;font-size:7.4px;line-height:9.5px;color:#333">Lorem ipsum dolor sit amet, consectetur adipiscing elit. Sed nisi neque, pharetra vel vehicula a, molestie quis tortor. Donec ut dui nec neque condimentum adipiscing. Sed pellentesque nisi in tellus congue pellentesque. Etiam a auctor tortor. Curabitur sollicitudin accumsan mauris vel faucibus. Proin accumsan leo at arcu accumsan semper. Phasellus justo lorem, sagittis quis sodales in, porta posuere velit.</p>
    <div class="narrow" style="position:absolute;left:245px;top:119px;width:101px;height:24px;border-radius:12px;background:linear-gradient(#7a7672,#565350);color:#fff;font-weight:700;font-size:10.5px;line-height:24px;text-align:center">LEARN MORE &#10095;</div>
  </div>
  <div style="position:absolute;left:0;top:284px;width:574px;height:110px;background:linear-gradient(#fff,#f2f2f2);border-bottom:1px dotted #cfcfcf">
    <div style="position:absolute;left:27px;top:20px;width:110px"><div class="narrow" style="font-size:11px;font-weight:700;color:#333">Horticulture Containers</div><p style="font-size:6px;line-height:7.9px;margin-top:3px">Lorem ipsum dolor sit amet, consectetur adipiscing elit. Sed nisi neque, pharetra vel vehicula a, molestie quis tortor. Donec ut dui nec neque condimentum adipiscing.</p><div class="narrow" style="margin-top:10px;font-size:7.5px;font-weight:700;color:var(--link)">&#8250; READ MORE</div></div>
    <div style="position:absolute;left:166px;top:20px;width:110px"><div class="narrow" style="font-size:11px;font-weight:700;color:#333">Agriculture Films</div><p style="font-size:6px;line-height:7.9px;margin-top:3px">Lorem ipsum dolor sit amet, consectetur adipiscing elit. Sed nisi neque, pharetra vel vehicula a, molestie quis tortor. Donec ut dui nec neque condimentum adipiscing.</p><div class="narrow" style="margin-top:10px;font-size:7.5px;font-weight:700;color:var(--link)">&#8250; READ MORE</div></div>
    <div style="position:absolute;left:310px;top:20px;width:110px"><div class="narrow" style="font-size:11px;font-weight:700;color:#333">Where to Buy</div><p style="font-size:6px;line-height:7.9px;margin-top:3px">Lorem ipsum dolor sit amet, consectetur adipiscing elit. Sed nisi neque, pharetra vel vehicula a, molestie quis tortor. Donec ut dui nec neque condimentum adipiscing.</p><div class="narrow" style="margin-top:10px;font-size:7.5px;font-weight:700;color:var(--link)">&#8250; READ MORE</div></div>
    <div style="position:absolute;left:448px;top:20px;width:110px"><div class="narrow" style="font-size:11px;font-weight:700;color:#333">Upcoming Products</div><p style="font-size:6px;line-height:7.9px;margin-top:3px">Lorem ipsum dolor sit amet, consectetur adipiscing elit. Sed nisi neque, pharetra vel vehicula a, molestie quis tortor. Donec ut dui nec neque condimentum adipiscing.</p><div class="narrow" style="margin-top:10px;font-size:7.5px;font-weight:700;color:var(--link)">&#8250; READ MORE</div></div>
  </div>
  <h2 style="position:absolute;left:18px;top:414px">Welcome to <b>Meadowline Bioplastics</b></h2>
  <p style="position:absolute;left:18px;top:440px;width:541px">Lorem ipsum dolor sit amet, consectetur adipiscing elit. Sed nisi neque, pharetra vel vehicula a, molestie quis tortor. Donec ut dui nec neque condimentum adipiscing. Sed pellentesque nisi in tellus congue pellentesque. Etiam a auctor tortor. Curabitur sollicitudin accumsan mauris vel faucibus. Proin accumsan leo at arcu accumsan semper. Phasellus justo lorem, sagittis quis sodales in, porta posuere velit. Nulla tellus nibh, auctor sed faucibus vitae, adipiscing at arcu. Cras odio ante, fringilla eu commodo in, elementum eget felis. Mauris nec ante diam. In auctor neque at tellus suscipit et gravida lectus mollis. Mauris dui dui, commodo et tristique eget, condimentum id quam. Nam auctor, urna sed tincidunt dictum, ligula diam bibendum mauris, eu consequat ipsum nibh at mi. Cum sociis natoque penatibus et magnis dis parturient montes, nascetur ridiculus mus. Quisque scelerisque vestibulum enim, in vestibulum mi rhoncus eget. Integer sagittis commodo turpis vel scelerisque. Vestibulum eget sapien at enim tincidunt sollicitudin eget aliquam ante. Proin tortor erat, sodales ut gravida nec, congue quis velit.</p>
  <p style="position:absolute;left:18px;top:522px;width:541px">Fusce quis erat lectus, eu congue risus. In hac habitasse platea dictumst. Nunc dolor erat, vestibulum consectetur tristique in, vestibulum a arcu. Curabitur risus tellus, porttitor quis eleifend sit amet, iaculis sed urna. Cras eget ultricies nisl. Morbi consectetur ipsum id urna consequat consequat. Mauris facilisis porttitor magna, vel varius erat pretium vel.</p>
  <ul class="ticks" style="position:absolute;left:42px;top:574px;width:502px">
    <li><svg width="7" height="6" viewBox="0 0 7 6"><path d="M.5 3.2 2.6 5 6.5.8" fill="none" stroke="#3aa61a" stroke-width="1.2"/></svg>Fusce quis erat lectus, eu congue risus. In hac habitasse platea dictumst. Nunc dolor erat, vestibulum consectetur tristique in, vestibulum a arcu. Curabitur risus tellus, porttitor quis eleifend sit amet, iaculis sed urna.</li>
    <li><svg width="7" height="6" viewBox="0 0 7 6"><path d="M.5 3.2 2.6 5 6.5.8" fill="none" stroke="#3aa61a" stroke-width="1.2"/></svg>Duis mauris dui, vestibulum vel cursus vitae, lobortis ac nibh. Duis volutpat scelerisque odio. Suspendisse consequat turpis augue, non ultrices neque.</li>
    <li><svg width="7" height="6" viewBox="0 0 7 6"><path d="M.5 3.2 2.6 5 6.5.8" fill="none" stroke="#3aa61a" stroke-width="1.2"/></svg>Curabitur sit amet lectus ut lorem vestibulum interdum euismod dictum lorem. Vivamus venenatis felis in ligula porttitor faucibus. Praesent gravida velit in erat ornare venenatis. Mauris eget urna id tellus imperdiet tincidunt.</li>
  </ul>
</section>
<footer class="footer" style="top:674px"><span>&copy; Copyright 2010 Meadowline Bioplastics. All rights reserved.</span><nav><a>Home</a> | <a>About Us</a> | <a>Products</a> | <a>Business Partners</a> | <a>Press Releases</a> | <a>Contact Us</a></nav></footer>

<!-- About Us template -->
<section class="page" style="top:694px;height:474px">
  <div class="header">
    <div class="brand"><i></i>Meadowline Bioplastics</div>
    <div class="phone">Contact Us Today! <b>(123) 456 789</b></div>
  </div>
  <div class="nav">
    <span style="left:11px">Home</span><span class="dd" style="left:54px">About Us</span><span class="dd" style="left:108px">Products</span><span style="left:166px">Business Partners</span><span style="left:255px">Press Releases</span><span style="left:329px">Contact Us</span>
    <div class="search"><svg width="9" height="9" viewBox="0 0 9 9"><circle cx="3.6" cy="3.6" r="2.6" fill="none" stroke="#777" stroke-width="1.1"/><line x1="5.5" y1="5.5" x2="8.3" y2="8.3" stroke="#777" stroke-width="1.3"/></svg>Search</div>
    <div class="submit">SUBMIT</div>
  </div>
  <div style="position:absolute;left:0;top:104px;width:574px;height:46px;background:linear-gradient(90deg,var(--mint) 60%,#e4f7e0);border-bottom:1px solid #b9e2b0">
    <div class="narrow" style="position:absolute;left:12px;top:6px;font-size:27px;color:var(--brand)">About Us</div>
  </div>
  <div class="photo" role="img" aria-label="Brown bird feather" style="left:449px;top:105px;width:110px;height:66px"></div>
  <h2 style="position:absolute;left:18px;top:172px">All about <b>Meadowline Bioplastics</b></h2>
  <p style="position:absolute;left:18px;top:195px;width:375px">Lorem ipsum dolor sit amet, consectetur adipiscing elit. Sed nisi neque, pharetra vel vehicula a, molestie quis tortor. Donec ut dui nec neque condimentum adipiscing. Sed pellentesque nisi in tellus congue pellentesque. Etiam a auctor tortor. Curabitur sollicitudin accumsan mauris vel faucibus. Proin accumsan leo at arcu accumsan semper. Phasellus justo lorem, sagittis quis sodales in, porta posuere velit. Nulla tellus nibh, auctor sed faucibus vitae, adipiscing at arcu. Cras odio ante, fringilla eu commodo in, elementum eget felis. Mauris nec ante diam. In auctor neque at tellus suscipit et gravida lectus mollis. Mauris dui dui, commodo et tristique eget, condimentum id quam. Nam auctor, urna sed tincidunt dictum, ligula diam bibendum mauris, eu consequat ipsum nibh at mi. Cum sociis natoque penatibus et magnis dis parturient montes, nascetur ridiculus mus. Quisque scelerisque vestibulum enim, in vestibulum mi rhoncus eget. Integer sagittis commodo turpis vel scelerisque. Vestibulum eget sapien at enim tincidunt sollicitudin eget aliquam ante. Proin tortor erat, sodales ut gravida nec, congue quis velit.</p>
  <p style="position:absolute;left:18px;top:305px;width:375px">Fusce quis erat lectus, eu congue risus. In hac habitasse platea dictumst. Nunc dolor erat, vestibulum consectetur tristique in, vestibulum a arcu. Curabitur risus tellus, porttitor quis eleifend sit amet, iaculis sed urna. Cras eget ultricies nisl. Morbi consectetur ipsum id urna consequat consequat. Mauris facilisis porttitor magna, vel varius erat pretium vel.</p>
  <ul class="ticks" style="position:absolute;left:42px;top:349px;width:352px;font-weight:700">
    <li><svg width="7" height="6" viewBox="0 0 7 6"><path d="M.5 3.2 2.6 5 6.5.8" fill="none" stroke="#3aa61a" stroke-width="1.2"/></svg>Fusce quis erat lectus, eu congue risus. In hac habitasse platea dictumst. Nunc dolor erat, vestibulum consectetur tristique in, vestibulum a arcu. Curabitur risus tellus, porttitor quis eleifend sit amet, iaculis sed urna.</li>
    <li><svg width="7" height="6" viewBox="0 0 7 6"><path d="M.5 3.2 2.6 5 6.5.8" fill="none" stroke="#3aa61a" stroke-width="1.2"/></svg>Duis mauris dui, vestibulum vel cursus vitae, lobortis ac nibh. Duis volutpat scelerisque odio. Suspendisse consequat turpis augue, non ultrices neque.</li>
    <li><svg width="7" height="6" viewBox="0 0 7 6"><path d="M.5 3.2 2.6 5 6.5.8" fill="none" stroke="#3aa61a" stroke-width="1.2"/></svg>Curabitur sit amet lectus ut lorem vestibulum interdum euismod dictum lorem. Vivamus venenatis felis in ligula porttitor faucibus. Praesent gravida velit in erat ornare venenatis. Mauris eget urna id tellus imperdiet tincidunt.</li>
  </ul>
  <nav class="subnav" style="position:absolute;left:425px;top:197px;width:138px;border:1px solid #dcdcdc;background:#f3f3f3;font-size:7px;font-weight:700;color:#444">
    <div style="height:21.5px;line-height:21.5px;padding-left:12px;border-bottom:1px solid #e2e2e2">Company Description</div>
    <div style="height:21.5px;line-height:21.5px;padding-left:12px;border-bottom:1px solid #e2e2e2;background:#e2e2e2;color:#999">Vision &amp; Statement</div>
    <div style="height:21.5px;line-height:21.5px;padding-left:12px;border-bottom:1px solid #e2e2e2">Vision &amp; Statement</div>
    <div style="height:21.5px;line-height:21.5px;padding-left:12px;border-bottom:1px solid #e2e2e2">Core Values &amp; Beliefs</div>
    <div style="height:21.5px;line-height:21.5px;padding-left:12px">Business Goals</div>
  </nav>
</section>
<footer class="footer" style="top:1179px"><span>&copy; Copyright 2010 Meadowline Bioplastics. All rights reserved.</span><nav><a>Home</a> | <a>About Us</a> | <a>Products</a> | <a>Business Partners</a> | <a>Press Releases</a> | <a>Contact Us</a></nav></footer>

</body>
</html>
```